Hottest Internet Based Blues Radio Station in Southwest Florida All Blues 24/7 Real Authentic Blues Classic and Modern

Business

Marco "Tall Ned" Okafor
The Harbor Airwaves, Inc.
514 Willow Crest Lane
Cedar Hollow, GA 33871

```html
<!DOCTYPE html>
<html lang="en">
<head>
<meta charset="UTF-8">
<title>Harbor Airwaves – Business Card</title>
<link href="https://fonts.googleapis.com/css2?family=Open+Sans:wght@400;600;700&display=swap" rel="stylesheet">
<style>
  :root {
    --stage: #3b3532;
    --card: #141414;
    --card-edge: #1f1f1f;
    --accent: #e8761e;
    --text: #d9d9d9;
    --rule: #6a6a6a;
    --silver: #cfcfcf;
    --silver-deep: #4a4a4a;
    --art-hot: #d2691e;
    --art-deep: #5a2a0c;
  }
  * { margin: 0; padding: 0; box-sizing: border-box; }
  html, body { width: 1200px; height: 814px; overflow: hidden; }
  body {
    background: var(--stage);
    font-family: "Open Sans", Arial, sans-serif;
    position: relative;
  }
  .card {
    position: absolute;
    top: 257px;
    width: 520px;
    height: 300px;
    background: var(--card);
    border: 1px solid var(--card-edge);
    box-shadow: 0 8px 24px rgba(0,0,0,.45);
  }
  .card--front { left: 60px; }
  .card--back {
    left: 620px;
    display: flex;
    flex-direction: column;
    align-items: center;
    justify-content: center;
    gap: 16px;
  }

  .brand { position: absolute; left: 34px; top: 50px; width: 210px; height: 200px; }
  .brand__art {
    position: absolute; left: 20px; top: 0; width: 170px; height: 145px;
    border-radius: 50%;
    background: radial-gradient(circle at 50% 45%, var(--art-hot), var(--art-deep) 70%, transparent 72%);
  }
  .brand__name {
    position: absolute; left: 0; right: 0; top: 160px;
    text-align: center;
    white-space: nowrap;
    color: #f2f2f2;
    font-weight: 600;
    font-size: 18px;
    letter-spacing: 1.5px;
  }

  .divider { position: absolute; left: 262px; top: 58px; width: 1px; height: 180px; background: var(--rule); }

  .contact { position: absolute; left: 284px; top: 66px; color: var(--text); font-size: 13px; line-height: 20px; }
  .contact__name { color: var(--accent); font-weight: 700; font-size: 16px; margin-bottom: 6px; white-space: nowrap; }
  .contact p { white-space: nowrap; }
  .contact__line { display: flex; align-items: center; gap: 8px; }
  .contact__line svg { width: 12px; height: 12px; fill: var(--accent); flex: none; }
  .contact__gap { height: 4px; }

  .back__art {
    width: 190px; height: 150px;
    border-radius: 50%;
    background: radial-gradient(circle at 50% 45%, var(--silver), var(--silver-deep) 70%, transparent 72%);
  }
  .back__name { color: var(--silver); font-weight: 600; font-size: 24px; letter-spacing: 2px; white-space: nowrap; }
</style>
</head>
<body>
  <section class="card card--front">
    <div class="brand">
      <div class="brand__art" role="img" aria-label="Fiery bird illustration with guitars, in orange tones"></div>
      <div class="brand__name">HARBOR AIRWAVES</div>
    </div>
    <div class="divider"></div>
    <div class="contact">
      <p class="contact__name">Marco "Tall Ned" Okafor</p>
      <p>The Harbor Airwaves, Inc.</p>
      <p>514 Willow Crest Lane</p>
      <p>Cedar Hollow, GA 33871</p>
      <div class="contact__gap"></div>
      <p class="contact__line">
        <svg viewBox="0 0 24 24" aria-hidden="true"><path d="M6.6 10.8a15.1 15.1 0 0 0 6.6 6.6l2.2-2.2c.3-.3.7-.4 1-.2 1.1.4 2.3.6 3.6.6.6 0 1 .4 1 1V20c0 .6-.4 1-1 1A17 17 0 0 1 3 4c0-.6.4-1 1-1h3.5c.6 0 1 .4 1 1 0 1.3.2 2.5.6 3.6.1.3 0 .7-.2 1z"/></svg>
        555 214 7390
      </p>
      <p class="contact__line">
        <svg viewBox="0 0 24 24" aria-hidden="true"><path d="M2 5h20v14H2z M2 5l10 8 10-8" stroke="#141414" stroke-width="1.5"/></svg>
        name@harborairwaves.com
      </p>
    </div>
  </section>

  <section class="card card--back">
    <div class="back__art" role="img" aria-label="Silver foil bird illustration"></div>
    <div class="back__name">HARBOR AIRWAVES</div>
  </section>
</body>
</html>
```